Clever & creative business card needed for a pediatric dentist.

We need a business card for a pediatric dentist that is building a brand-new pediatric dental practice. He is funny, outgoing, and sociable, and he hopes to give his business card to dentists and pediatricians so that he can give them information of where to refer infants, children, and teenagers that need high quality and attainable dental care.

The name of the dental practice is Copper Fern Pediatric Dentistry. Logo design .png / .pdf/ .jpg are provided to aid in the design.

The dentist's last name is Tolvan (which sounds like "burger", as in "hamburger” or “cheeseburger"). Since it is pediatric practice, kudos will be given to designs that implement a little joke into the design - but hopefully in a small or hidden way (such as putting something like a cheeseburger on the back of the card, or hiding it an an abstract way).

Thank you!

Please make a design that incorporates colors. It should be fun! Not too serious. It does not have to follow the color scheme of the logos.

```html
<!DOCTYPE html>
<html lang="en">
<head>
<meta charset="utf-8">
<title>Copper Fern Pediatric Dentistry — Business Card</title>
<link rel="stylesheet" href="https://fonts.googleapis.com/css2?family=Quicksand:wght@500;600&family=Lato:wght@300;400&display=swap">
<style>
  :root {
    --backdrop: #b2c5b9;
    --card-front: #f5f5f7;
    --card-front-panel: #dcdcde;
    --card-back: #575a56;
    --card-back-shade: #4f524e;
    --brand-green: #4c9a66;
    --mint: #a9d4ad;
    --ink-grey: #5a5a5a;
    --ink-white: #f4f4f2;
  }
  * { margin: 0; padding: 0; box-sizing: border-box; }
  html, body { width: 1200px; height: 800px; overflow: hidden; }
  body { background: var(--backdrop); position: relative; font-family: "Lato", sans-serif; }

  .card {
    position: absolute;
    left: 364px;
    width: 484px;
    height: 277px;
    border-radius: 30px;
    overflow: hidden;
  }
  .card--front { top: 106px; background: var(--card-front); }
  .card--back { top: 424px; background: var(--card-back); }

  .front-panel {
    position: absolute;
    top: 0; right: 0;
    width: 256px; height: 100%;
    background: var(--card-front-panel);
    border-radius: 120px 0 0 0;
  }

  .brand { position: absolute; text-align: left; font-family: "Quicksand", sans-serif; font-weight: 600; }
  .brand__mark { display: block; border-radius: 50%; }
  .brand__name { display: block; line-height: 1; }
  .brand__tagline { display: block; text-transform: uppercase; line-height: 1; }

  .brand--front { left: 35px; top: 26px; color: var(--ink-grey); }
  .brand--front .brand__mark { width: 34px; height: 34px; background: var(--mint); margin: 0 0 10px 40px; }
  .brand--front .brand__name { font-size: 21px; }
  .brand--front .brand__tagline { font-size: 6.5px; letter-spacing: 2.6px; margin-top: 5px; }

  .holder { position: absolute; left: 51px; top: 149px; font-size: 15px; line-height: 1; }
  .holder__name { font-family: "Quicksand", sans-serif; font-weight: 600; color: var(--brand-green); }
  .holder__role { font-weight: 300; color: var(--ink-grey); margin-top: 1px; }

  .contact-list { position: absolute; left: 34px; top: 190px; list-style: none; }
  .contact-list li { display: flex; align-items: center; font-size: 14.5px; font-weight: 300; color: var(--ink-grey); height: 16.5px; }
  .contact-list svg { width: 11px; height: 11px; margin-right: 6px; flex: none; }
  .website { position: absolute; left: 51px; top: 244px; font-size: 14.5px; color: var(--brand-green); font-weight: 400; }

  .brand--back { left: 0; width: 100%; top: 76px; text-align: center; color: var(--ink-white); }
  .brand--back .brand__mark { width: 62px; height: 62px; background: var(--mint); margin: 0 auto 18px; }
  .brand--back .brand__name { font-size: 30px; }
  .brand--back .brand__tagline { font-size: 11px; letter-spacing: 5px; margin-top: 8px; }

  .burger-art {
    position: absolute;
    right: 0; top: 0;
    width: 128px; height: 100%;
    background: linear-gradient(180deg, var(--card-back) 0%, var(--card-back-shade) 40%, var(--card-back-shade) 100%);
    border-radius: 70px 0 0 70px;
  }
</style>
</head>
<body>

  <section class="card card--front">
    <div class="front-panel"></div>

    <div class="brand brand--front">
      <span class="brand__mark"></span>
      <span class="brand__name">copper fern</span>
      <span class="brand__tagline">Pediatric Dentistry</span>
    </div>

    <div class="holder">
      <p class="holder__name">Dana Tolvan</p>
      <p class="holder__role">Dentistry</p>
    </div>

    <ul class="contact-list">
      <li>
        <svg viewBox="0 0 12 12" aria-hidden="true"><circle cx="6" cy="6" r="5.2" fill="none" stroke="#4c9a66" stroke-width="1"/><path d="M6 2.6a2 2 0 0 1 2 2c0 1.5-2 3.8-2 3.8S4 6.1 4 4.6a2 2 0 0 1 2-2z" fill="none" stroke="#4c9a66" stroke-width="0.9"/><circle cx="6" cy="4.6" r="0.7" fill="#4c9a66"/></svg>
        4180 Marlow Ave Ste 12
      </li>
      <li>
        <svg viewBox="0 0 12 12" aria-hidden="true"><circle cx="6" cy="6" r="5.2" fill="none" stroke="#4c9a66" stroke-width="1"/><path d="M4 3.2l1 1.2-.6.8c.4.9 1 1.5 1.9 1.9l.8-.6 1.2 1-.6 1c-2.3-.2-4.1-2-4.3-4.3z" fill="#4c9a66"/></svg>
        +1 000-000-0000
      </li>
      <li>
        <svg viewBox="0 0 12 12" aria-hidden="true"><circle cx="6" cy="6" r="5.2" fill="none" stroke="#4c9a66" stroke-width="1"/><rect x="3.4" y="4.2" width="5.2" height="3.6" fill="none" stroke="#4c9a66" stroke-width="0.8"/><path d="M3.4 4.2L6 6.2l2.6-2" fill="none" stroke="#4c9a66" stroke-width="0.8"/></svg>
        info@copperfern.com
      </li>
    </ul>

    <p class="website">www.copperfern.com</p>
  </section>

  <section class="card card--back">
    <div class="brand brand--back">
      <span class="brand__mark"></span>
      <span class="brand__name">copper fern</span>
      <span class="brand__tagline">Pediatric Dentistry</span>
    </div>
    <div class="burger-art" role="img" aria-label="Faint tone-on-tone cheeseburger illustration peeking in from the right edge"></div>
  </section>

</body>
</html>
```